Lumora Learning Web Design Project

Who We are:
Lumora Learning is education information portal/ magazine, providing information about the Chinese and International education markets. Our aim is to help school principals improve there curriculum, and parents in understanding this curriculum.

Project Brief:
The site will include education news updates, educational services, curriculum developments and overseas study. We hope the site represents the cross cultural bridge between the west and east. The site will cover both the Sciences and Arts.

Note:
The logo design competition is also underway so we only need the website design

What We want:
This competition is for Design only no coding!
Design a home page based on Template 1,2 or 3. I only need to select one.
The design of an article page.

Optional
Design a Microsoft Windows metro style splash page.

Sites We like:
http://www.kavelin.com.cn/kavelinlingo/default.aspx
http://www.brixtalacademia.co.uk/
http://qrpv.norvatestudio.net/

Template Explanations:
Template 1-
The main information has a dynamic sliding category view that when clicked displays the relevant info.
In addition to the main upper menu it also has a left hand sliding menu that pops out on click or gesture

Template 2-
Has limited number of Articles most of the menus are drop downs from the top menu

Template 3-
No Top menu

Target Market(s)

Teachers, principals and parents

Industry/Entity Type

Education

Requirements
Should not have
• kindergarten preschool feel

```html
<!DOCTYPE html>
<html lang="en">
<head>
<meta charset="utf-8">
<title>Lumora Learning</title>
<link href="https://fonts.googleapis.com/css2?family=Bitter:wght@400;700&family=Oswald:wght@500;700&family=Open+Sans:wght@400;600;700&display=swap" rel="stylesheet">
<style>
:root{
  --red:#c8161d;
  --red-dark:#9e1016;
  --blue:#1b3f7e;
  --blue-dark:#142f60;
  --yellow:#e6c21a;
  --ink:#2a2a2a;
  --grey-text:#777;
  --panel:#e9e9e9;
  --dark:#2b2b2b;
  --footer-light:#efefef;
}
*{box-sizing:border-box;margin:0;padding:0}
html,body{width:760px;height:1200px;overflow:hidden}
body{position:relative;font-family:"Open Sans",Arial,sans-serif;color:var(--ink);
  background:linear-gradient(180deg,#a8a29c 0,#d8d4d0 180px,#e6e4e2 600px,#e6e4e2 870px);}
.abs{position:absolute}
.page-bg{left:0;top:0;width:760px;height:870px;background:
  radial-gradient(ellipse at 60px 120px,#8f877f 0,rgba(143,135,127,0) 220px),
  radial-gradient(ellipse at 700px 90px,#9b938b 0,rgba(155,147,139,0) 200px);}
.top-links{left:116px;top:11px;font-size:6px;color:#fff;letter-spacing:.2px;word-spacing:1px}
.top-links span{margin:0 4px}
.lang{left:567px;top:11px;font-size:6px;color:#fff}
.lang-box{left:624px;top:9px;width:20px;height:11px;background:#fff;border-radius:1px}
.lang-box i{position:absolute;left:3px;top:3px;width:8px;height:5px;background:var(--blue)}
.lang-box b{position:absolute;left:13px;top:5px;border:2px solid transparent;border-top-color:#555}

.dark-band{left:0;top:870px;width:760px;height:256px;background:var(--dark)}
.footer-light{left:0;top:1126px;width:760px;height:74px;background:var(--footer-light)}

.card{left:115px;top:30px;width:529px;height:892px;background:#fff;box-shadow:0 0 6px rgba(0,0,0,.25)}

.call{left:136px;top:64px;font-size:6px;color:#666}
.call strong{display:block;font-size:9.5px;color:var(--blue);font-weight:600;margin-top:1px}
.logo{left:330px;top:48px;width:100px;text-align:center}
.logo .dot{width:26px;height:26px;border-radius:50%;background:var(--red);margin:0 auto 4px}
.logo .name{font-size:9px;font-weight:700;color:var(--blue);letter-spacing:.2px}
.search{left:508px;top:62px;width:117px;height:19px;border:1px solid #ddd;font-size:5px;color:#888;padding:6px 9px}
.search svg{position:absolute;right:6px;top:4px}

.nav{left:134px;top:103px;width:491px;height:23px;background:var(--blue);display:flex}
.nav a{font-family:"Bitter",Georgia,serif;font-weight:700;font-size:7.6px;color:#fff;text-decoration:none;
  padding:0 7.1px;line-height:23px;border-right:1px solid #2e549a}
.nav a.on{background:var(--red)}

.hero{left:134px;top:140px;width:337px;height:177px;background:linear-gradient(135deg,#8a9068 0,#b49a48 35%,#6c6a55 60%,#b8b6ab 100%);overflow:hidden}
.hero .line1{position:absolute;left:74px;top:112px;font-family:"Oswald",sans-serif;font-weight:500;font-size:17px;color:#fff;transform:rotate(-6deg);letter-spacing:.5px}
.hero .line2{position:absolute;left:70px;top:124px;font-family:"Oswald",sans-serif;font-weight:700;font-size:42px;color:#e7b92a;transform:rotate(-6deg);letter-spacing:-.5px}
.hero .credit{position:absolute;right:2px;bottom:6px;font-size:5px;color:#fff;writing-mode:vertical-rl;transform:rotate(180deg)}
.hero .next{position:absolute;left:312px;top:76px;width:17px;height:17px;border-radius:50%;background:rgba(255,255,255,.45)}

.side-panel{background:var(--panel)}
.ptitle{position:absolute;left:10px;top:10px;width:126px;height:18px;background:var(--red);color:#fff;
  font-family:"Bitter",Georgia,serif;font-weight:700;font-size:8px;line-height:18px;padding-left:20px}
.ptitle small{position:absolute;right:8px;top:0;font-family:"Open Sans",sans-serif;font-size:5px;font-weight:600;text-decoration:underline}
.ptitle i{position:absolute;left:7px;top:5px;width:8px;height:8px;background:#fff;opacity:.85}
.books{left:480px;top:140px;width:145px;height:177px}
.book{position:absolute;left:10px;width:125px}
.book .cover{position:absolute;left:0;top:0;width:34px;height:50px}
.book h4{position:absolute;left:40px;top:0;width:86px;font-size:5.6px;font-weight:400;line-height:7.5px;color:#222}
.book p{position:absolute;left:40px;width:86px;font-size:5px;line-height:6.6px;color:#888}

.cat-head{left:134px;top:333px;width:338px;height:24px;background:var(--blue);color:#fff;
  font-family:"Bitter",Georgia,serif;font-weight:700;font-size:11.5px;line-height:24px;padding-left:12px;letter-spacing:.2px}
.cat-body{left:134px;top:357px;width:338px;height:371px;background:var(--panel)}
.thumb{position:absolute;left:9px;width:149px;height:62px}
.cap{position:absolute;left:9px;font-size:5.6px;color:#333}
.cat-list{position:absolute;left:184px;top:16px;width:142px;list-style:none}
.cat-list li{height:16.3px;line-height:16px;border-bottom:1px solid #d7d7d7;font-family:"Bitter",Georgia,serif;font-weight:700;font-size:7.2px;color:#222;padding-left:18px;position:relative}
.cat-list li::before{content:"";position:absolute;left:6px;top:5px;width:6px;height:6px;border-radius:50%;background:#333}
.cat-list li.on{background:var(--red);color:#fff;border-bottom-color:var(--red)}
.cat-list li.on::before{background:#fff}

.features{left:480px;top:333px;width:145px;height:189px;background:var(--dark)}
.features .art{position:absolute;left:10px;top:30px;width:126px;height:96px;background:linear-gradient(135deg,#c79a5a 0,#e0bf84 45%,#b2794a 100%)}
.features h5{position:absolute;left:11px;top:135px;font-size:5.6px;color:#fff;font-weight:600}
.features p{position:absolute;left:11px;top:148px;width:124px;font-size:5.6px;line-height:7px;color:#aaa}

.ad{left:480px;top:534px;width:145px;height:194px;background:linear-gradient(180deg,#7fb83a 0,#8cc23f 70%,#e4a81e 93%)}
.ad .head{position:absolute;left:6px;top:6px;font-family:"Oswald",sans-serif;font-weight:700;font-size:20px;line-height:20px;color:#fff;text-transform:uppercase}
.ad .pic{position:absolute;left:60px;top:80px;width:85px;height:100px;background:linear-gradient(160deg,#6b4a38 0,#3b2a22 60%,#b81f2a 100%);opacity:.85}

.countries{left:134px;top:742px;width:338px;list-style:none}
.countries li{height:19px;margin-bottom:1.5px;background:var(--blue);color:#fff;font-family:"Bitter",Georgia,serif;font-weight:700;font-size:6.4px;line-height:19px;padding-left:19px;position:relative;text-transform:uppercase}
.countries li i{position:absolute;left:8px;top:7px;width:7px;height:5px}
.countries li span{position:absolute;right:10px;top:0;font-weight:400;font-size:5.6px}
.countries li.on{background:var(--yellow);color:var(--ink)}

.popular{left:480px;top:742px;width:145px;height:164px}
.tabs{position:absolute;left:10px;top:6px;display:flex}
.tabs div{height:18px;line-height:18px;font-size:6.2px;padding:0 6px 0 15px;position:relative}
.tabs div::before{content:"";position:absolute;left:5px;top:6px;width:6px;height:6px}
.tabs .t1{background:var(--red);color:#fff}.tabs .t1::before{background:#fff;border-radius:50%}
.tabs .t2{background:var(--yellow);color:#333;margin-left:3px}.tabs .t2::before{border:1px solid #333}
.popular ul{position:absolute;left:10px;top:32px;list-style:none}
.popular li{font-size:5.5px;font-weight:600;color:#333;height:12.4px;padding-left:10px;position:relative;white-space:nowrap}
.popular li::before{content:"";position:absolute;left:0;top:1.5px;width:4px;height:4px;background:#ccc}

.ribbon{left:94px;width:21px;color:#fff;font-family:"Bitter",Georgia,serif;font-weight:700;font-size:6px;
  writing-mode:vertical-rl;transform:rotate(180deg);text-align:center;display:flex;align-items:center;justify-content:center;text-transform:uppercase}
.ribbon.red{background:var(--red)}
.ribbon.yellow{background:var(--yellow);color:#333}

.social{left:644px;top:230px;width:22px;height:122px;background:#3a3a3a;border-radius:0 3px 3px 0}
.social i{position:absolute;left:7px;width:8px;height:8px;border-radius:50%;background:#ddd}

.footer-h{font-family:"Bitter",Georgia,serif;font-weight:700;font-size:9px;color:#d7262c;text-transform:uppercase}
.reasons{left:116px;top:948px;width:135px}
.reasons .lead{font-size:5.6px;color:#fff;font-weight:600;line-height:8px;margin-top:6px;text-transform:uppercase}
.reasons ul{list-style:none;margin-top:6px}
.reasons li{font-size:5.6px;color:#ddd;line-height:7px;padding-left:10px;position:relative;margin-bottom:6px}
.reasons li::before{content:"";position:absolute;left:0;top:1px;width:5px;height:5px;background:#888}
.register{left:115px;top:1080px;width:127px;height:24px;background:var(--red);color:#fff;font-family:"Bitter",Georgia,serif;font-weight:700;font-size:9px;line-height:24px;padding-left:22px;border-bottom:2px solid var(--red-dark)}
.register svg{position:absolute;right:12px;top:7px}
.opinion-title{left:297px;top:948px}
.op{position:absolute;width:190px}
.op .pic{position:absolute;left:0;top:0;width:68px;height:50px}
.op h6{position:absolute;left:76px;top:0;width:112px;font-size:5.8px;font-weight:700;color:#fff;line-height:7.4px;text-transform:uppercase}
.op p{position:absolute;left:76px;width:85px;font-size:5.8px;color:#999;line-height:7.2px}

.f-logo{left:368px;top:1138px;width:24px;height:16px}
.f-logo i{position:absolute;left:0;top:0;width:15px;height:15px;border-radius:50%;background:var(--red)}
.f-links{left:0;top:1161px;width:760px;text-align:center;font-size:5.2px;color:#666;text-transform:uppercase;word-spacing:1px}
.f-links span{margin:0 4px}
.f-copy{left:0;top:1171px;width:760px;text-align:center;font-size:5.2px;color:#666;text-transform:uppercase}
</style>
</head>
<body>
<div class="abs page-bg"></div>
<div class="abs dark-band"></div>
<div class="abs footer-light"></div>

<div class="abs top-links">WELCOME <span>|</span> LOG IN <span>|</span> REGISTER <span>|</span> SUBSCRIBE</div>
<div class="abs lang">Select Language</div>
<div class="abs lang-box"><i></i><b></b></div>

<div class="abs ribbon red" style="top:104px;height:100px">Choral Festival On</div>
<div class="abs ribbon yellow" style="top:208px;height:72px">RTS Festival</div>
<div class="abs ribbon red" style="top:284px;height:120px">Spring Festival Concer</div>
<div class="abs ribbon red" style="top:408px;height:134px">Campus Spring Festival</div>

<div class="abs social">
  <i style="top:18px"></i><i style="top:33px"></i><i style="top:48px"></i><i style="top:63px"></i><i style="top:78px"></i><i style="top:93px"></i>
</div>

<div class="abs card"></div>

<div class="abs call">CALL NOW<strong>(180) 555-014-2297</strong></div>
<div class="abs logo"><div class="dot"></div><div class="name">LUMORA LEARNING</div></div>
<div class="abs search">SEARCH HERE
  <svg width="9" height="9" viewBox="0 0 10 10"><circle cx="4" cy="4" r="3" fill="none" stroke="#333" stroke-width="1.4"/><line x1="6.2" y1="6.2" x2="9.3" y2="9.3" stroke="#333" stroke-width="1.6"/></svg>
</div>

<nav class="abs nav">
  <a class="on">HOME</a><a>NEWS</a><a>COMMENT</a><a>FEATURES</a><a>BOOKS</a><a>RANKINGS</a><a>AWARDS</a><a>JOBS</a><a>SUBSCRIBE</a><a style="border:0">CONTACT US</a>
</nav>

<div class="abs hero" role="img" aria-label="Photo of smiling women farm workers outdoors">
  <div class="line1">REDEFINE</div>
  <div class="line2">#WOMENSWORK</div>
  <div class="next"><svg width="17" height="17" viewBox="0 0 17 17"><path d="M7 5l4 3.5-4 3.5" fill="none" stroke="#fff" stroke-width="1.8"/></svg></div>
  <div class="credit">Photo: Dara Keswick</div>
</div>

<section class="abs books side-panel">
  <div class="ptitle"><i></i>Books<small>View all</small></div>
  <div class="book" style="top:40px">
    <div class="cover" role="img" aria-label="Book cover with a dark portrait" style="background:linear-gradient(180deg,#3a3b45,#1d1e24)"></div>
    <h4>The Merchant Class: Between History and Literature by Emil Varant Subscription</h4>
    <p style="top:30px">Helen Marwick relishes this considered study of a quietly worthy class of men</p>
  </div>
  <div class="book" style="top:114px">
    <div class="cover" role="img" aria-label="White book cover with red and blue title" style="background:#f4f2ee;border:1px solid #223"></div>
    <h4>The Double Shift: How Working Women Are Creating a New Society by Clara Denholm</h4>
    <p style="top:30px">A better gender balance in government benefits all, Ruth Calloway observes</p>
  </div>
</section>

<div class="abs cat-head">CATEGORIES</div>
<section class="abs cat-body">
  <div class="thumb" style="top:20px;background:linear-gradient(135deg,#f29a1c,#e8661a)" role="img" aria-label="Orange banner with a trumpet announcing new online programs"></div>
  <div class="cap" style="top:92px">Charm School National Campus Spring Festiva</div>
  <div class="thumb" style="top:106px;background:linear-gradient(135deg,#2c3aa0,#6a3aa8 60%,#d7a02a)" role="img" aria-label="Campus arts festival poster with singers on stage"></div>
  <div class="cap" style="top:177px">Star Lin Weiyu," 2013 Campus Arts Festival</div>
  <div class="thumb" style="top:188px;background:linear-gradient(180deg,#c63a1a,#e0a020)" role="img" aria-label="Choir on a red stage at a campus choral festival"></div>
  <div class="cap" style="top:260px">Charm School National Campus Spring Festiva</div>
  <div class="thumb" style="top:274px;background:linear-gradient(135deg,#3a1d4e,#8a3aa0 55%,#d8a060)" role="img" aria-label="Performers on a purple lit stage"></div>
  <div class="cap" style="top:344px">Star Lin Weiyu," 2013 Campus Arts Festival</div>
  <ul class="cat-list">
    <li>Children's rights education</li>
    <li class="on">Sciences</li>
    <li>Deaf education</li>
    <li>Childhood Longitudinal Program</li>
    <li>Educology</li>
    <li>Teaching and learning center</li>
    <li>History of Education</li>
    <li>School supplies</li>
    <li>QuickNotes</li>
    <li>Financial Education</li>
    <li>Adventure learning</li>
    <li>Children's Film Unit</li>
    <li>University Programs</li>
    <li>Education Rights</li>
    <li>Financial Education</li>
    <li>Brain Works</li>
    <li>Syllabus</li>
    <li>Course atlas</li>
    <li>Teacher look</li>
    <li>First day of school</li>
  </ul>
</section>

<section class="abs features">
  <div class="ptitle"><i></i>Features<small>View all</small></div>
  <div class="art" role="img" aria-label="Painting of a reclining figure in warm ochre tones"></div>
  <h5>IDENTITY CRISIS FOR WOMEN'S STUDIES</h5>
  <p>Nora Pellham on why the erosion of women's, gender and sexuality studies in UK universities is cause for concern ipsum is simply dummy text of the...</p>
</section>

<section class="abs ad" role="img" aria-label="Reading campaign advert with a girl holding a red book">
  <div class="pic"></div>
  <div class="head">Being a<br>good reader<br>doesn't<br>help</div>
</section>

<ul class="abs countries">
  <li><i style="background:#f29a2e"></i>India<span>HISTORY</span></li>
  <li class="on"><i style="background:var(--blue)"></i>Australia<span>DRAMA</span></li>
  <li><i style="background:#d8281e"></i>China<span>SCIENCES</span></li>
  <li><i style="background:#d8281e"></i>Costa Rica<span>ENGLISH</span></li>
  <li><i style="background:#d8281e"></i>Egypt<span>HISTORY</span></li>
  <li><i style="background:#3a5ab0"></i>France<span>LANGUAGE</span></li>
  <li><i style="background:#e0b020"></i>Germany<span>DARAMA</span></li>
  <li><i style="background:#2a9a4a"></i>Italy<span>ENGLISH</span></li>
</ul>

<section class="abs popular side-panel">
  <div class="tabs"><div class="t1">Most Popular</div><div class="t2">Commented</div></div>
  <ul>
    <li>Postgrad support boosted as numbers</li>
    <li>How not to write a PhD thesis</li>
    <li>Obesity Tweet "not part of research"</li>
    <li>Liverpool students 'receive wrong</li>
    <li>Harlow regime reviews university policies</li>
    <li>Leaders show how to build gay-friendly</li>
    <li>BA Scholarly Web - 27 June 2013</li>
    <li>IEDO: opening the market door will</li>
    <li>Thalias celebrations led by Newcastle</li>
    <li>NSP change embarrassing for Lib</li>
  </ul>
</section>

<section class="abs reasons">
  <div class="footer-h">Reasons to register</div>
  <p class="lead">Registering with the website is quick, easy and free and there are so many reasons to sign up...</p>
  <ul>
    <li>Sample BA articles every month</li>
    <li>Get your weekly higher education update in our newsletters</li>
    <li>Debate the latest developments by commenting on BA stories</li>
    <li>Set up your own job alerts</li>
    <li>ave stories into your online library</li>
  </ul>
</section>
<div class="abs register">REGISTER NOW
  <svg width="9" height="9" viewBox="0 0 10 10"><path d="M1 9l1-3 5-5 2 2-5 5z" fill="#fff"/></svg>
</div>

<div class="abs footer-h opinion-title">Opinion</div>
<div class="op" style="left:297px;top:968px">
  <div class="pic" role="img" aria-label="Illustration of laboratory flasks" style="background:linear-gradient(135deg,#f0e0c0,#d84a2a)"></div>
  <h6>'Big science', big hype, big mistake</h6>
  <p style="top:22px">We are paying too high a price for 100,000 genomes more, warns Neil Varco</p>
</div>
<div class="op" style="left:484px;top:968px">
  <div class="pic" role="img" aria-label="Illustration of a hand pointing at blue figures" style="background:linear-gradient(135deg,#fff 30%,#2a2a2a 50%,#3a8ad8 80%)"></div>
  <h6>New practice in student admissions</h6>
  <p style="top:22px">The sector will be damaged if integrity in recruitment is lost, says Joan Arkell</p>
</div>
<div class="op" style="left:297px;top:1044px">
  <div class="pic" role="img" aria-label="Illustration of figures in academic gowns" style="background:linear-gradient(135deg,#f2d890,#3a5ab0 60%,#d84a2a)"></div>
  <h6>Hollis's lessons for the academy</h6>
  <p style="top:22px">The inquiry's recommendations echo a similar arrangement in higher education, Tom Ellery says</p>
</div>
<div class="op" style="left:484px;top:1044px">
  <div class="pic" role="img" aria-label="Pencil sketch portrait" style="background:linear-gradient(135deg,#fafafa,#bdbdbd)"></div>
  <h6>A breath of 'fresh' air</h6>
  <p style="top:14px">Martin Quill loved Aberystwyth, despite the respiratory hazards</p>
</div>

<div class="abs f-logo"><i></i></div>
<div class="abs f-links">How to advertise <span>|</span> Terms &amp; conditions <span>|</span> Privacy policy <span>|</span> Feedback <span>|</span> Cookie policy <span>|</span> Help</div>
<div class="abs f-copy">Copyright © 2013 Lumoralearning</div>
</body>
</html>
```